Brightline Villas Estepona listings flyer

Brightline Villas Estepona are a specialist estate agency focussed solely on selling modern and contemporary homes.

We need an A4 folded flyer to be designed so that Brightline Villas Estepona can leaflet drop all of the modern homes for sale in our area to generate new instructions / listings. We need to engage with owners of those types of homes by posting this marketing material through their letter boxes in the hope that they see our funky and modern design and decide to call us about our services to sell their home, if for sale.

We would like to see sharp lines and a modern design (see our logo for style and colour scheme), with lots of white spaces and using photos which can blend in to the background to provide a powerful and impacting image to set us aside from any other direct mail leaflets which may be in their post box. It needs to show

* Quality
* Style
* Modern and forward thinking in design and outlook
* Professionalism

Front page
Top:
Logo of Brightline Villas Estepona.
Helping you sell your modern home. It’s all we do!

4 property photos in a grid position

Bottom banner
If you are thinking of selling, read on…

INSIDE LEFT & RIGHT (DOUBLE PAGE POSSIBLY BLANK WHITE BACKGROUND)
Title: Use Brightline Villas Estepona – the specialist modern homes agency to sell your home

We bring an exciting and dynamic mix of modern marketing with good old fashioned service to guarantee only the most qualified clients will be viewing your home (use online marketing image)

Marketing packages include stylish online brochures, professional photography, stunning drone video footage, informative video walk thru’s and unique floor plans (use drone and floor plan images)

Targeted social media campaigns focusing on international clientele actively looking to buy property in southern Spain (use social media image)

Bespoke, powerful advertising packages enable worldwide exposure for both online and traditional channels to market. We can be as discreet or as visible as you want us to be to sell your home

During our 20 years on the Costa del Sol, we have built up an enviable network of collaborating agents meaning you only have to instruct one expert real estate agent, Brightline Villas Estepona, to gain maximum exposure for your home

BACK PAGE

If you want service that matches the value of your home, contact us today for a private, personalised consultation. Brightline Villas Estepona. It’s all we do.

Suite 14
Torrenova Office Park
Calle Los Almendros
Valdemoro, Marbella

Tel: +34 952 418 306
Mobil y Whatsapp: +34 677 342 815
Email: info@brightlinevillasestepona.example
www.brightlinevillasestepona.example

Target Market(s)

Wealthy property owners of contemporary and modern homes who are looking to sell their home

Industry/Entity Type

Real Estate Agent

Font styles to use
Serif
Sans Serif

Colors
606060
e7e7e7
f5f5f5

Requirements
Must have
• Classy, professional, modern design with the ability to stand out from other leaflet drops / direct mail in letter box
Nice to have
• straight lines to border photos
• Maybe extend the lines further than they should so it has the look of an architects plan
• Blend in images to white background in the middle open double page
Should not have
• Lots of different colours

```html
<!DOCTYPE html>
<html lang="en">
<head>
<meta charset="utf-8">
<title>Brightline Villas Estepona – Selling Flyer</title>
<link rel="stylesheet" href="https://fonts.googleapis.com/css2?family=Inter:wght@400;600;700&display=swap">
<style>
  :root{
    --teal:#52c1cd;
    --teal-text:#3db8c6;
    --ink:#606060;
    --ink-dark:#3f3f3f;
    --white:#ffffff;
    --paper:#ffffff;
  }
  *{margin:0;padding:0;box-sizing:border-box}
  html,body{width:1200px;height:1200px;overflow:hidden;background:var(--paper)}
  body{position:relative;font-family:"Inter",Helvetica,Arial,sans-serif;color:var(--ink)}
  .abs{position:absolute}

  /* back panel */
  .invite{left:250px;top:83px;width:316px;text-align:center;color:var(--teal-text);font-size:12px;line-height:15.5px}
  .signoff{left:220px;top:142px;width:376px;text-align:center;color:var(--teal-text);font-size:12.6px;font-weight:700;letter-spacing:.2px}
  .contact-panel{left:210px;top:370px;width:396px;height:224px;background:var(--teal)}
  .photo{display:block}
  .photo-back{left:258px;top:179px;width:299px;height:199px;background:linear-gradient(180deg,#4c9ce6 0%,#a9d2f3 38%,#f2f4f4 55%,#78a95c 72%,#3b86cf 100%)}
  .contact-row{position:absolute;left:112px;color:var(--white);font-size:11px;line-height:13.6px}
  .contact-icon{position:absolute;left:76px}

  /* front cover */
  .brand{left:686px;top:120px;width:260px;display:flex;align-items:center;justify-content:center;gap:10px}
  .brand-mark{width:14px;height:14px;background:var(--ink)}
  .brand-name{font-size:16px;font-weight:600;letter-spacing:1.2px;color:var(--ink);text-transform:uppercase}
  .cover-rule{left:606px;top:190px;width:397px;height:4px;background:var(--teal)}
  .photo-cover{left:606px;top:194px;width:397px;height:258px;background:linear-gradient(180deg,#1f72c8 0%,#6fb0e6 35%,#f4f4f2 55%,#8cb86a 68%,#3fa6d8 78%,#86cdec 100%)}
  .thumbs{left:606px;top:452px;width:397px;height:68px;display:flex}
  .thumb{flex:1;height:100%}
  .thumb-online{background:linear-gradient(135deg,#5b8fb0,#d9dee2)}
  .thumb-plan{background:linear-gradient(135deg,#f4f4f4,#dcdcdc)}
  .thumb-social{background:linear-gradient(135deg,#0b1a4a,#2b4fa8)}
  .thumb-drone{background:linear-gradient(180deg,#c6d3ea,#e6ecf5)}
  .cover-banner{left:606px;top:526px;width:397px;height:68px;background:var(--teal);color:var(--white);font-size:15px;display:flex;align-items:center;justify-content:center;letter-spacing:.2px}

  /* inside spread */
  .photo-inside-left{left:210px;top:606px;width:396px;height:272px;background:linear-gradient(180deg,#7fb2e2 0%,#e9eef2 30%,#f6f6f6 60%,#6cb33e 82%,#7fd0ea 100%)}
  .photo-inside-right{left:608px;top:606px;width:397px;height:272px;background:linear-gradient(180deg,#2a6dc4 0%,#eef1f2 35%,#e7e9e8 60%,#6f9b3f 85%,#5d7f34 100%)}
  .title-card{left:236px;top:844px;width:346px;height:56px;background:var(--white)}
  .spread-title{left:210px;top:866px;width:398px;text-align:center;color:var(--teal-text);font-size:12.8px;font-weight:700;line-height:15.5px;letter-spacing:.2px}
  .body-copy{width:200px;font-size:9.8px;line-height:16px;color:var(--ink)}
  .body-copy p+p{margin-top:16px}
  .copy-left{left:314px;top:938px}
  .copy-right{left:714px;top:938px}
</style>
</head>
<body>

  <!-- Back page -->
  <p class="abs invite">If you want service that matches the value of your home, contact us today for a private, personalised consultation.</p>
  <p class="abs signoff">Brightline Villas Estepona. It’s all we do.</p>

  <section class="abs contact-panel">
    <svg class="contact-icon" style="top:40px" width="22" height="22" viewBox="0 0 22 22" fill="none" stroke="#fff" stroke-width="1.3">
      <path d="M2 11 L11 3 L20 11"/><path d="M5 9 V20 H17 V9"/><path d="M9 20 V14 H13 V20"/>
    </svg>
    <div class="contact-row" style="top:23px">Suite 14<br>Torrenova Office Park<br>Calle Los Almendros<br>Valdemoro, Marbella</div>

    <svg class="contact-icon" style="top:96px" width="24" height="24" viewBox="0 0 24 24" fill="#fff">
      <path d="M6.6 3.5c.6-.4 1.4-.2 1.8.4l2 3.3c.3.6.2 1.3-.3 1.7l-1.4 1.1c.9 2 2.5 3.7 4.5 4.7l1.2-1.3c.4-.5 1.2-.6 1.7-.3l3.3 2c.6.4.8 1.2.4 1.8l-1.2 1.9c-.6.9-1.7 1.3-2.7 1C9.8 18.3 5.7 14.2 4.2 8.1c-.3-1 .1-2.1 1-2.7z"/>
    </svg>
    <div class="contact-row" style="top:104px;left:116px">+34 952 418 306<br>+34 677 342 815</div>

    <svg class="contact-icon" style="top:147px" width="24" height="18" viewBox="0 0 24 18" fill="none" stroke="#fff" stroke-width="1.3">
      <rect x="1" y="1" width="22" height="16"/><path d="M1 1 L12 10 L23 1"/><path d="M1 17 L9 8"/><path d="M23 17 L15 8"/>
    </svg>
    <div class="contact-row" style="top:149px">info@brightlinevillasestepona.example</div>

    <svg class="contact-icon" style="top:177px" width="23" height="23" viewBox="0 0 24 24" fill="none" stroke="#fff" stroke-width="1.2">
      <circle cx="12" cy="12" r="10.5"/><ellipse cx="12" cy="12" rx="4.5" ry="10.5"/><path d="M1.5 12 H22.5 M3.5 6.5 H20.5 M3.5 17.5 H20.5 M12 1.5 V22.5"/>
    </svg>
    <div class="contact-row" style="top:183px">www.brightlinevillasestepona.example</div>
  </section>

  <div class="abs photo photo-back" role="img" aria-label="White modern villa with a blue pool and timber deck under a clear sky"></div>

  <!-- Front cover -->
  <div class="abs brand">
    <span class="brand-mark"></span>
    <span class="brand-name">Brightline Villas Estepona</span>
  </div>
  <div class="abs cover-rule"></div>
  <div class="abs photo photo-cover" role="img" aria-label="Large white two-storey villa with terracotta roof behind a wide turquoise pool"></div>
  <div class="abs thumbs">
    <div class="thumb thumb-online" role="img" aria-label="Hand sketching an online marketing plan on a tablet"></div>
    <div class="thumb thumb-plan" role="img" aria-label="Architectural floor plan drawing"></div>
    <div class="thumb thumb-social" role="img" aria-label="Phone screen showing social media app icons"></div>
    <div class="thumb thumb-drone" role="img" aria-label="Camera drone in flight against a pale sky"></div>
  </div>
  <div class="abs cover-banner">If you are thinking of selling, read on…</div>

  <!-- Inside spread -->
  <div class="abs photo photo-inside-left" role="img" aria-label="Row of white contemporary townhouses above a lawn and small pool"></div>
  <div class="abs photo photo-inside-right" role="img" aria-label="White modern homes with terraces, palm trees and sun loungers on a lawn"></div>
  <div class="abs title-card"></div>
  <h2 class="abs spread-title">Use Brightline Villas Estepona – the<br>specialist modern homes agency to sell your home</h2>

  <div class="abs body-copy copy-left">
    <p>We bring an exciting and dynamic mix of modern marketing with good old fashioned service to guarantee only the most qualified clients will be viewing your home.</p>
    <p>Marketing packages include stylish online brochures, professional photography, stunning drone video footage, informative video walk thru’s and unique floor plans Targeted social media campaigns focusing on international clientele actively looking to buy property in southern Spain.</p>
  </div>
  <div class="abs body-copy copy-right">
    <p>Bespoke, powerful advertising packages enable worldwide exposure for both online and traditional channels to market. We can be as discreet or as visible as you want us to be to sell your home.</p>
    <p>During our 20 years on the Costa del Sol, we have built up an enviable network of collaborating agents meaning you only have to instruct one expert real estate agent, Brightline Villas Estepona, to gain maximum exposure for your home.</p>
  </div>

</body>
</html>
```